Web Design Project: Facility Management company

Hi! We need a new website.

Our current website: http://www.vireo-trade.ru/ and we don-t like it. =)
The structure of our company has changed and now we don't need "cleaning" and "engeneering" on this site.

We are facility management company in Russia. So we provide integrated service solutions specific to industrial services: maintenance, repair, etc. of engineering systems.
More services:
Energy planning
Automation
Audit
Statements with regulators
Video surveillance
Central heating
Security systems
Welding
Management of subcontractors
Electrical installation and service needs
Reception
Catering

Visitors:
* Managers in the field of commercial real estate
* Chief engineers
* TOP managers of large companies, malls, factories...
+ their subordinates
* Small% of applicants.

Here you can see some websites/patterns we liked:
http://www.kobalmire.ru/ (This is our competitor’s site, so our site shouldn’t be an exact copy))))
http://www.dwatqo.ru/
http://www.layoutfarrow.com/demo/24296.html
http://www.layoutfarrow.com/website-templates/10145.html

Style:
Light, hi-tech/minimalizm, the color palette should be based on the original site colors (Green + black + white). http://www.vireo-trade.ru/

Estimated sitemap:
1. Home
2. About Us
3. Company's policy
4. History + Achievements.
5. Certificates
6. Map of presence (Here you can use sample map in file "our projects")
7. Services
8. Portfolio
9. News or blog
10. Jobs
11. Contacts - with the feedback form (or the function "call to order")
12. English

Need a design pages: main page, page 404. The rest of the page could be created by general pattern.

Logo, navigation bar and contacts should be visible on all pages of a site.
Flash animation elements and buttons, etc. - not needed.

* We need to develop 3 websites, so we are looking for a long term cooperation.
Looking forward to your creativity =)

Must Have:
Clear, intuitive structure of web pages.
In the center - of pictures reflecting our main services (industrial theme). May be in rotation.
BUT! This banner (central picture) should not be a huge one =)
All relevant information should be visible at once without scrolling.

A possibility to place media files (presentations, video ...) and 2 banner links on the main page.

Font should be available in Cyrillic.
Updates

IMPORTANT!

Please notice that in thisdesign we don't need "cleaning" and "engeneering" on this site.

So don't use old block of 4pictures from our current website. We don't need it anymore. 

Thestructure of our company has changed and now we need some links (may be banners,may be something else) to our future cleaning website as well as engeneeringwebsite.
It should look like seperate (partner) companies, not like our sevices.

Regards, Vera.

Please don't forget that we need bilingual site.

So define language changing tool in your designs.

Industry/Entity Type

Industrial

```html
<!DOCTYPE html>
<html lang="en">
<head>
<meta charset="utf-8">
<title>Vireo Trade — Facility Management</title>
<link rel="stylesheet" href="https://fonts.googleapis.com/css2?family=Didact+Gothic&family=PT+Sans:wght@400;700&family=PT+Sans+Narrow&display=swap">
<style>
:root{
  --green:#c6e86a;
  --green-btn:#bfe36a;
  --ink:#1c1c1c;
  --text:#3a3a3a;
  --muted:#666;
  --panel:#e8e8e8;
  --line:#bdbdbd;
  --link:#2f7fc1;
  --page:#ffffff;
  --outside:#efefef;
}
*{margin:0;padding:0;box-sizing:border-box}
html,body{width:1200px;height:1060px;overflow:hidden}
body{background:var(--outside);font-family:"PT Sans",Arial,sans-serif;color:var(--text);position:relative}
.top-bar{position:absolute;left:0;top:0;width:1200px;height:4px;background:var(--green)}
.page{position:absolute;left:153px;top:4px;width:894px;height:1056px;background:var(--page);border-left:1px solid #ddd;border-right:1px solid #ddd}
.abs{position:absolute}

.brand{left:159px;top:23px;width:218px;height:58px;display:flex;align-items:center;gap:10px}
.brand-mark{width:26px;height:26px;background:var(--ink)}
.brand-name{font-family:"Didact Gothic",sans-serif;font-size:24px;letter-spacing:3px;color:var(--ink)}

.lang{left:790px;top:19px;font-size:12px;color:var(--muted);display:flex;gap:5px}
.lang a{color:var(--muted);text-decoration:none}
.lang a.current{color:var(--ink);font-weight:700}

.search{left:865px;top:13px;width:172px;height:28px;border-radius:14px;background:linear-gradient(#fff,#ececec);border:1px solid #d3d3d3;box-shadow:1px 2px 2px rgba(0,0,0,.15);font-size:12px;color:#333;padding:6px 12px;display:flex;justify-content:space-between;align-items:center}
.phone{right:165px;top:54px;display:flex;align-items:center;gap:10px;font-size:22px;color:var(--ink)}

.nav{left:163px;top:96px;width:874px;height:31px;background:linear-gradient(#2a2a2a,#050505);border-radius:6px;display:flex;align-items:center;padding-left:12px;box-shadow:0 2px 3px rgba(0,0,0,.3)}
.nav a{color:#fff;text-decoration:none;font-size:12px;padding:0 14px;height:31px;line-height:31px;border-right:1px solid #3d3d3d}
.nav a:last-child{border-right:0}
.nav a.active{background:var(--green);color:#333;border-radius:4px;height:29px;line-height:29px;margin-right:8px;border-right:0}

.hero{left:164px;top:134px;width:873px;height:279px;border-radius:8px;background:linear-gradient(100deg,#8ba4bd 0%,#c9d3dc 30%,#3a4a5a 55%,#d7d9d9 75%,#6a6a68 100%);box-shadow:0 2px 3px rgba(0,0,0,.3)}
.arrow{width:43px;height:31px;background:#1a1a1a;display:flex;align-items:center;justify-content:center}
.arrow.left{border-radius:0 5px 5px 0}
.arrow.right{border-radius:5px 0 0 5px}
.arrow.boxed{border-radius:5px}

.col{top:416px;width:283px;height:262px;background:var(--panel);box-shadow:0 6px 5px -4px rgba(0,0,0,.45)}
.col h2,.box h2{font-family:"Didact Gothic",sans-serif;font-weight:400;font-size:24px;color:#222;padding-bottom:6px;border-bottom:1px solid var(--line)}
.col h2{position:absolute;left:9px;top:9px;width:261px}
.welcome p{position:absolute;left:7px;top:56px;width:270px;font-size:11.5px;line-height:18.5px;color:#333}
.btn-more{background:var(--green-btn);font-family:"PT Sans Narrow",sans-serif;font-size:17px;color:#222;width:81px;height:32px;display:flex;align-items:center;justify-content:center}
.svc-photo{left:14px;top:59px;width:93px;height:169px;background:linear-gradient(160deg,#b98a5a,#9aa7b0 45%,#c8cdd1)}
.svc-list{left:121px;top:56px;list-style:none}
.svc-list li{font-family:"Didact Gothic",sans-serif;font-size:15px;color:#222;margin-bottom:18px;display:flex;align-items:center;gap:8px}
.svc-list li:before{content:"";border-left:6px solid #222;border-top:5px solid transparent;border-bottom:5px solid transparent}
.news-item{left:34px;width:226px;height:68px;border-bottom:1px solid var(--line);display:flex;gap:18px}
.news-icon{width:14px;height:14px;border:1px solid #aab;margin-top:4px;flex:none;background:repeating-linear-gradient(#fff 0 2px,#aab 2px 3px)}
.news-item p{font-size:11.5px;line-height:18.5px;color:#333}
.news-item a{color:var(--link);text-decoration:none;display:block}

.newsletter{left:164px;top:711px;width:244px}
.newsletter h2{font-family:"Didact Gothic",sans-serif;font-weight:400;font-size:24px;color:#222;padding:0 0 6px 4px;border-bottom:1px solid var(--line);margin-bottom:15px}
.field{height:28px;border-radius:14px;background:#e6e6e6;border:1px solid #d0d0d0;font-size:11.5px;color:#444;padding:6px 12px;margin-bottom:8px}
.submit{margin-left:181px;width:63px;height:25px;border-radius:7px;background:#222;color:#fff;font-size:12px;display:flex;align-items:center;justify-content:center}

.box{left:435px;top:697px;width:600px;height:188px;background:#ebebeb}
.box h2{position:absolute;left:19px;top:8px;width:571px}
.thumb{top:66px;width:183px;height:101px}

.footer{left:163px;top:897px;width:874px;height:153px;border-radius:8px 8px 0 0;background:linear-gradient(#2c2c2c,#050505);color:#fff;text-align:center;font-size:11px}
.follow{position:absolute;left:0;right:0;top:34px;display:flex;justify-content:center;align-items:center;gap:6px}
.follow span{margin-right:4px}
.social{width:17px;height:17px;border-radius:3px;background:#5d7fb0}
.f-links{position:absolute;left:85px;right:85px;top:74px;border-top:1px solid #444;padding-top:13px}
.f-links a{color:#fff;text-decoration:none}
.f-links i{font-style:normal;margin:0 6px}
.copy{position:absolute;left:0;right:0;top:120px}
</style>
</head>
<body>
<div class="top-bar"></div>
<div class="page"></div>

<div class="abs brand"><span class="brand-mark"></span><span class="brand-name">VIREO TRADE</span></div>

<div class="abs lang"><a class="current" href="#">EN</a><span>|</span><a href="#">RU</a></div>
<div class="abs search"><span>Search</span>
  <svg width="14" height="14" viewBox="0 0 14 14"><circle cx="5.5" cy="5.5" r="4" fill="none" stroke="#777" stroke-width="1.5"/><line x1="8.5" y1="8.5" x2="13" y2="13" stroke="#777" stroke-width="2"/></svg>
</div>
<div class="abs phone">
  <svg width="30" height="22" viewBox="0 0 30 22"><path d="M4 18 V12 A11 11 0 0 1 26 12 V18" fill="none" stroke="#111" stroke-width="3"/><rect x="1" y="12" width="6" height="9" rx="2" fill="#111"/><rect x="23" y="12" width="6" height="9" rx="2" fill="#111"/></svg>
  <span>+7 812 555 0148</span>
</div>

<nav class="abs nav">
  <a class="active" href="#">Home</a><a href="#">About Us</a><a href="#">Company's policy</a><a href="#">History</a><a href="#">Certificates</a><a href="#">Locations Map</a><a href="#">Services</a><a href="#">Portfolio</a><a href="#">Blog</a><a href="#">Jobs</a><a href="#">Contact Us</a>
</nav>

<div class="abs hero" role="img" aria-label="Photo of two engineers in hard hats at a construction site"></div>
<div class="abs arrow left" style="left:152px;top:238px"><svg width="12" height="14"><path d="M9 1 L3 7 L9 13" fill="none" stroke="#fff" stroke-width="2.5"/></svg></div>
<div class="abs arrow right" style="left:1005px;top:238px"><svg width="12" height="14"><path d="M3 1 L9 7 L3 13" fill="none" stroke="#fff" stroke-width="2.5"/></svg></div>

<section class="abs col welcome" style="left:168px">
  <h2>Welcome to our site</h2>
  <p>These are the most important aspects of acquisition of the highest possible incomes from the commercial property object`s operation regardless of their purpose: it can be production, business center, a building of a shop, bank, restaurant, warehousing logistic complex, hotel or the biggest shopping and recreation center.</p>
  <div class="abs btn-more" style="left:7px;top:192px">Get More</div>
</section>

<section class="abs col" style="left:457px">
  <h2 style="left:18px;width:252px">Services</h2>
  <div class="abs svc-photo" role="img" aria-label="Photo of a worker in an orange hard hat holding documents"></div>
  <ul class="abs svc-list">
    <li>Maintenance</li>
    <li>Automation</li>
    <li>Security Systems</li>
  </ul>
  <div class="abs btn-more" style="left:118px;top:192px">Get More</div>
</section>

<section class="abs col" style="left:747px">
  <h2 style="left:14px;width:270px">News</h2>
  <div class="abs news-item" style="top:58px"><span class="news-icon"></span><p>We use an accumulated experience of immovable property...<a href="#">Read More</a></p></div>
  <div class="abs news-item" style="top:126px"><span class="news-icon"></span><p>We use an accumulated experience of immovable property...<a href="#">Read More</a></p></div>
  <div class="abs news-item" style="top:195px;border-bottom:0"><span class="news-icon"></span><p>We use an accumulated experience of immovable property...<a href="#">Read More</a></p></div>
</section>

<section class="abs newsletter">
  <h2>Newsletter</h2>
  <div class="field">Enter the name</div>
  <div class="field">Enter the E mail id</div>
  <div class="submit">Submit</div>
</section>

<section class="abs box">
  <h2>Portfolio</h2>
  <div class="abs thumb" style="left:19px;background:linear-gradient(135deg,#aaa,#ddd 50%,#8a8a8a)" role="img" aria-label="Photo of metal pipes"></div>
  <div class="abs thumb" style="left:213px;background:linear-gradient(135deg,#f4e04a,#dde6ea 55%,#2e6fa8)" role="img" aria-label="Photo of a gloved hand cleaning tiles"></div>
  <div class="abs thumb" style="left:406px;background:linear-gradient(135deg,#e9ecef,#c4cad0)" role="img" aria-label="Photo of rolled technical blueprints"></div>
  <div class="abs arrow boxed" style="left:0;top:97px"><svg width="12" height="14"><path d="M9 1 L3 7 L9 13" fill="none" stroke="#fff" stroke-width="2.5"/></svg></div>
  <div class="abs arrow boxed" style="left:557px;top:97px"><svg width="12" height="14"><path d="M3 1 L9 7 L3 13" fill="none" stroke="#fff" stroke-width="2.5"/></svg></div>
</section>

<footer class="abs footer">
  <div class="follow"><span>Follow Us on</span><i class="social"></i><i class="social"></i><i class="social"></i><i class="social" style="background:#e08a2a"></i></div>
  <div class="f-links">
    <a href="#">Home</a><i>|</i><a href="#">About Us</a><i>|</i><a href="#">Company's policy</a><i>|</i><a href="#">History + Achievements.</a><i>|</i><a href="#">Certificates</a><i>|</i><a href="#">Locations Map</a><i>|</i><a href="#">Services</a><i>|</i><a href="#">Portfolio</a><i>|</i><a href="#">Blog</a><i>|</i><a href="#">Jobs</a><i>|</i><a href="#">Contacts</a>
  </div>
  <div class="copy">Copyrights @ 2012 All Rights Reserved</div>
</footer>
</body>
</html>
```